Flyer "Pinch Analysis"-Energy Optimization procedure for Industry

We need a flyer (1xA4 recto/verso )design for a new part of our business.

In Summary: we want to communicate that we are providing "Pinch Analysis" for the industry. It's an energy optimization procedure. We are a cutting edge engineering consulting group.

All details about project in the attached files

Target Market(s)

Engineering

Industry/Entity Type

Business

Font styles to use
Serif

Requirements
Must have
• Finale document in .ai format ready for printing
• More informations in attached files
Nice to have
• See attached files

```html
<!DOCTYPE html>
<html lang="fr">
<head>
<meta charset="utf-8">
<title>Analyse Pinch – Korvel Engineering</title>
<link href="https://fonts.googleapis.com/css2?family=Orbitron:wght@400;500;800;900&family=Roboto+Condensed:wght@700&display=swap" rel="stylesheet">
<style>
  :root{
    --sky-deep:#2a4c9c;
    --sky-mid:#3f6cc0;
    --sky-glow:#eaf4ff;
    --brand-cyan:#5cc3ee;
    --band-cyan:#5bbde3;
    --navy:#0f2a55;
    --white:#ffffff;
    --plant-blue:#3d8fc9;
    --plant-grey:#b9c4cc;
    --hot-curve:#0d2a5c;
    --cold-curve:#4fb6e6;
    --grid:#26436f;
  }
  html,body{margin:0;padding:0;overflow:hidden;background:#fff;}
  .flyer{position:relative;width:849px;height:1200px;overflow:hidden;background:var(--white);font-family:"Orbitron",sans-serif;}
  .sky{position:absolute;left:0;top:0;width:849px;height:276px;
    background:
      radial-gradient(circle at 586px 102px, var(--sky-glow) 0 18px, rgba(220,236,255,.8) 40px, rgba(120,160,230,.35) 130px, transparent 230px),
      linear-gradient(180deg, var(--sky-mid) 0%, var(--sky-deep) 100%);}
  .brand{position:absolute;left:84px;top:163px;margin:0;font-family:"Orbitron",sans-serif;font-weight:800;
    font-size:56px;letter-spacing:4px;color:var(--brand-cyan);line-height:1;}
  .title-band{position:absolute;left:0;top:289px;width:849px;height:222px;
    background:linear-gradient(180deg, rgba(91,189,227,.95), rgba(110,200,235,.9));}
  .plant-photo{position:absolute;left:0;top:511px;width:849px;height:689px;
    background:
      linear-gradient(90deg, rgba(40,110,170,.9) 0 90px, transparent 90px 170px),
      linear-gradient(90deg, transparent 200px, rgba(175,185,195,.85) 210px 290px, transparent 300px),
      linear-gradient(180deg, #9ec7e4 0%, var(--plant-blue) 45%, #8fa3b2 75%, var(--plant-grey) 100%);}
  .headline{position:absolute;left:79px;top:314px;margin:0;}
  .headline .main{display:block;font-weight:900;font-size:50px;letter-spacing:3px;color:var(--navy);line-height:1;}
  .headline .sub{display:block;margin-top:14px;font-weight:400;font-size:33px;letter-spacing:2.5px;color:var(--white);line-height:41px;}
  .overlay{position:absolute;left:0;top:0;}
  .axis-num{font-family:"Roboto Condensed",sans-serif;font-weight:700;font-size:7px;fill:var(--navy);}
  .chart-title{font-family:"Roboto Condensed",sans-serif;font-weight:700;font-size:11px;fill:var(--navy);letter-spacing:.3px;}
  .axis-label{font-family:"Roboto Condensed",sans-serif;font-weight:700;font-size:9.5px;fill:var(--navy);letter-spacing:.6px;}
</style>
</head>
<body>
<div class="flyer">
  <div class="sky" role="img" aria-label="Ciel bleu avec soleil éclatant"></div>
  <p class="brand">KORVEL</p>

  <div class="plant-photo" role="img" aria-label="Photo d’une installation industrielle : cuves bleues, tuyauteries inox et vannes"></div>
  <div class="title-band"></div>

  <h1 class="headline">
    <span class="main">ANALYSE PINCH -</span>
    <span class="sub">EN ROUTE VERS<br>LA PERFORMANCE<br>ÉNERGÉTIQUE</span>
  </h1>

  <svg class="overlay" width="849" height="1200" viewBox="0 0 849 1200">
    <!-- pipe frame -->
    <g fill="none" stroke="var(--white)" stroke-width="6" stroke-linecap="round">
      <path d="M849 700 H790 Q770 700 770 720 V860"/>
      <path d="M849 745 H810 Q790 745 790 765 V900"/>
      <path d="M849 920 H815 Q795 920 795 940 V1145 Q795 1165 775 1165 H480 Q460 1165 460 1185 V1200"/>
      <path d="M849 955 H830 Q812 955 812 973 V1175"/>
      <path d="M420 1200 V1190 Q420 1170 440 1170"/>
    </g>
    <rect x="378" y="860" width="414" height="282" rx="22" fill="rgba(255,255,255,.78)" stroke="var(--white)" stroke-width="6"/>
    <rect x="368" y="916" width="20" height="6" fill="var(--white)"/>
    <rect x="765" y="818" width="14" height="6" fill="var(--white)"/>

    <text class="chart-title" x="421" y="891">HOT AND COLD COMPOSITE CURVES</text>

    <!-- grid -->
    <g stroke="var(--grid)" stroke-width=".8" opacity=".85">
      <line x1="440" y1="904" x2="440" y2="1089"/><line x1="480.3" y1="904" x2="480.3" y2="1089"/>
      <line x1="520.6" y1="904" x2="520.6" y2="1089"/><line x1="560.9" y1="904" x2="560.9" y2="1089"/>
      <line x1="601.2" y1="904" x2="601.2" y2="1089"/><line x1="641.5" y1="904" x2="641.5" y2="1089"/>
      <line x1="681.8" y1="904" x2="681.8" y2="1089"/><line x1="722.1" y1="904" x2="722.1" y2="1089"/>
      <line x1="762.4" y1="904" x2="762.4" y2="1089"/>
      <line x1="440" y1="904" x2="762.4" y2="904"/><line x1="440" y1="927.1" x2="762.4" y2="927.1"/>
      <line x1="440" y1="950.3" x2="762.4" y2="950.3"/><line x1="440" y1="973.4" x2="762.4" y2="973.4"/>
      <line x1="440" y1="996.4" x2="762.4" y2="996.4"/><line x1="440" y1="1019.6" x2="762.4" y2="1019.6"/>
      <line x1="440" y1="1042.7" x2="762.4" y2="1042.7"/><line x1="440" y1="1065.9" x2="762.4" y2="1065.9"/>
    </g>
    <line x1="440" y1="1089" x2="762.4" y2="1089" stroke="var(--navy)" stroke-width="1.5"/>
    <line x1="440" y1="904" x2="440" y2="1089" stroke="var(--navy)" stroke-width="1.5"/>

    <g class="axis-num" text-anchor="end">
      <text x="436" y="1091">0</text><text x="436" y="1068">20</text><text x="436" y="1045">40</text>
      <text x="436" y="1022">60</text><text x="436" y="999">80</text><text x="436" y="976">100</text>
      <text x="436" y="953">120</text><text x="436" y="930">140</text><text x="436" y="907">160</text>
    </g>
    <g class="axis-num" text-anchor="middle">
      <text x="440" y="1100">0</text><text x="480.3" y="1100">100</text><text x="520.6" y="1100">200</text>
      <text x="560.9" y="1100">300</text><text x="601.2" y="1100">400</text><text x="641.5" y="1100">500</text>
      <text x="681.8" y="1100">600</text><text x="722.1" y="1100">700</text><text x="762.4" y="1100">800</text>
    </g>
    <text class="axis-label" transform="translate(413 1080) rotate(-90)">ACTUAL TEMPERATURE (°C)</text>
    <text class="axis-label" x="601" y="1122" text-anchor="middle">HEAT FLOW (kW)</text>

    <!-- composite curves -->
    <polyline points="468.2,1077.4 593.1,1019.6 609.9,930.5 734.2,930.5" fill="none" stroke="var(--cold-curve)" stroke-width="3.5"/>
    <polyline points="440,1069.3 492.4,1057.8 542.8,1030.8 546.8,1010.3" fill="none" stroke="var(--hot-curve)" stroke-width="3.5"/>
  </svg>
</div>
</body>
</html>
```